Professional consulting firm needing a Word document template

I need a Word document template that can be used flexibly for a flyer or brochure of 1 to 3 pages in length. The first page should be designed in a way that it can stand alone as a one-page flyer without a formal cover page. I have attached sample text as a Word document that could be used as the basis for the first 1-2 pages, however I do need three page layouts designed to give flexibility to use as a 3 page booklet. I have attached our brand guidelines, logo, and some stock images that I have previously purchased (they may not all be useful but it gives some options). <br/>The Word document needs to be set up in away that it can easily be edited to accommodate updates to the text, and some variation in the quantity of text on each page. Each page should be able to accommodate a mixture of paragraph text, bullet points, small boxes to call out highlights, one or more images, and some white space to avoid clutter. It should look professional yet engaging and modern.

Font styles to use
Sans Serif

Requirements
Must have
• Must be an editable Microsoft Word document, using the text provided. Must be a layout suitable to use as 1 page, up to 3 pages. Must comply with brand guidelines.

```html
<!DOCTYPE html>
<html lang="en">
<head>
<meta charset="utf-8">
<title>What is involved – Project Flyer</title>
<link href="https://fonts.googleapis.com/css2?family=Lato:wght@300;400;700&display=swap" rel="stylesheet">
<style>
  :root {
    --accent: #2bb5e3;
    --ink: #3d3d3d;
    --brand-dark: #1d3147;
    --paper: #ffffff;
    --blob-light: #62bfd0;
    --blob-deep: #4a9fd9;
  }
  * { margin: 0; padding: 0; box-sizing: border-box; }
  html, body { width: 848px; height: 1200px; overflow: hidden; background: var(--paper); }
  body { font-family: "Lato", Arial, sans-serif; color: var(--ink); }
  .page { position: relative; width: 848px; height: 1200px; }

  .header-graphic { position: absolute; left: 186px; top: 0; width: 476px; height: 172px; }

  .content { position: absolute; left: 146px; top: 228px; width: 548px; font-weight: 300; font-size: 13.2px; line-height: 19.6px; }
  .section-title { color: var(--accent); font-weight: 700; font-size: 14px; margin-bottom: 16px; }
  .content p { text-align: justify; margin-bottom: 13px; }

  .activity-list { list-style: none; margin: 0 0 16px 10px; }
  .activity-list li { margin-bottom: 0; }
  .activity-list li::before { content: "• "; color: var(--accent); font-weight: 700; }
  .activity-name { color: var(--accent); font-weight: 700; }

  .contact-block { position: absolute; right: 154px; top: 869px; text-align: right; font-weight: 300; font-size: 13.2px; line-height: 19.4px; }
  .contact-block .company { color: var(--accent); }

  .brand-mark { position: absolute; left: 0; right: 0; top: 1130px; text-align: center; font-weight: 700; font-size: 27px; letter-spacing: 2px; color: var(--brand-dark); }
</style>
</head>
<body>
<div class="page">
  <svg class="header-graphic" viewBox="0 0 476 172" role="img" aria-label="Decorative pattern of blue rounded cells forming a half-sphere">
    <defs>
      <linearGradient id="sphereTone" x1="0" y1="0" x2="1" y2="1">
        <stop offset="0" stop-color="var(--blob-deep)"/>
        <stop offset="1" stop-color="var(--blob-light)"/>
      </linearGradient>
    </defs>
    <path d="M0 0 H476 C476 95 370 168 238 168 C106 168 0 95 0 0 Z" fill="url(#sphereTone)" opacity="0.85"/>
  </svg>

  <main class="content">
    <h2 class="section-title">What is involved?</h2>
    <p>Participating organisations will be invited to provide in-kind support for the following activities during the period April – June 2020:</p>
    <ul class="activity-list">
      <li><span class="activity-name">Interviews with volunteer Driver participants:</span> individual discussions with our researchers about drivers’ previous experiences, to gather information about expert driving strategies and positive techniques used in normal and abnormal operations.</li>
      <li><span class="activity-name">Initial workshop:</span> a facilitated group workshop to understand the links between underlying competencies and driving tasks, and to understand Drivers’ perceptions of what each underlying competency looks like in practice.</li>
      <li><span class="activity-name">Driver Training Survey:</span> a voluntary survey will be distributed, requesting Driver Trainers’ and Assessors’ views on the importance of underlying competencies in driving performance, and further data about expert strategies and techniques.</li>
      <li><span class="activity-name">Follow-up workshop:</span> a facilitated group workshop to test and refine the performance indicators. Where possible, indicators will be tested through participants providing ratings of a video sample of actual performance, to determine whether multiple raters can distinguish between competency categories.</li>
    </ul>
    <p>It is anticipated that workshops will be run in Brisbane, Sydney and Melbourne. We would appreciate support from participating organisations in providing a workshop venue where possible. Apart from the in-kind support of providing access to personnel and a meeting room, there is no cost associated with participation in the project.</p>
    <p>In addition to the activities involving industry participation, we will also be completing a detailed task analysis and analysing incident reports and other publicly available data, to help inform the development of the framework.</p>
    <p>We look forward to hearing from organisations interested in being part of this landmark project.</p>
  </main>

  <address class="contact-block" style="font-style:normal">
    <div class="company">Company Name</div>
    <div>www.website.com.au</div>
    <div>contact@webbsite. com.au</div>
  </address>

  <div class="brand-mark">CORVANTIS</div>
</div>
</body>
</html>
```